I need a Professional Eye-Catching Paperback and e-Book Cover Design done with different mockups

I need a Professional Eye-Catching e-Book Cover Design done with different mockups

I need 2-3 designs to choose from per designer.

Book title - Lasting Harvest:

Subtitle - Growing riches beyond your years

Author name - K. Dapo Ramiro

I have attached some sample designs but i need you to be creative.

```html
<!DOCTYPE html>
<html lang="en">
<head>
<meta charset="UTF-8">
<title>Lasting Harvest — Book Cover</title>
<link href="https://fonts.googleapis.com/css2?family=Cinzel:wght@700&family=Montserrat:wght@500;600&display=swap" rel="stylesheet">
<style>
  :root {
    --green-deep: #133620;
    --green-mid: #1d4d2d;
    --green-glow: #27623a;
    --gold: #d9a743;
    --gold-light: #f3d27a;
    --gold-dark: #9c6f22;
  }
  * { margin: 0; padding: 0; box-sizing: border-box; }
  html, body {
    width: 800px;
    height: 1200px;
    overflow: hidden;
  }
  body { background: var(--green-deep); }
  .book-cover {
    position: relative;
    width: 800px;
    height: 1200px;
    background: radial-gradient(ellipse at 50% 50%, var(--green-glow) 0%, var(--green-mid) 45%, var(--green-deep) 100%);
    text-align: center;
    overflow: hidden;
  }
  .cover-title {
    position: absolute;
    top: 100px;
    left: 0;
    width: 100%;
    font-family: "Cinzel", "Times New Roman", serif;
    font-weight: 700;
    font-size: 118px;
    line-height: 1.02;
    letter-spacing: 6px;
    text-transform: uppercase;
    background: linear-gradient(180deg, var(--gold-light) 0%, var(--gold) 55%, var(--gold-dark) 100%);
    -webkit-background-clip: text;
    background-clip: text;
    color: transparent;
  }
  .title-rule {
    position: absolute;
    top: 366px;
    left: 130px;
    width: 540px;
    height: 3px;
    background: var(--gold);
  }
  .cover-subtitle {
    position: absolute;
    top: 388px;
    left: 0;
    width: 100%;
    font-family: "Montserrat", Arial, sans-serif;
    font-weight: 600;
    font-size: 26px;
    letter-spacing: 3px;
    text-transform: uppercase;
    color: var(--gold);
  }
  .cover-illustration {
    position: absolute;
    top: 460px;
    left: 170px;
    width: 470px;
    height: 580px;
    border-radius: 46% 54% 40% 60% / 38% 42% 58% 62%;
    background:
      radial-gradient(ellipse at 62% 28%, rgba(243, 210, 122, 0.95) 0%, rgba(217, 167, 67, 0.75) 22%, rgba(217, 167, 67, 0) 48%),
      radial-gradient(ellipse at 42% 72%, rgba(240, 200, 100, 0.9) 0%, rgba(190, 140, 50, 0.7) 28%, rgba(156, 111, 34, 0) 62%),
      radial-gradient(ellipse at 50% 50%, rgba(217, 167, 67, 0.45) 0%, rgba(29, 77, 45, 0) 72%);
  }
  .cover-author {
    position: absolute;
    bottom: 72px;
    left: 0;
    width: 100%;
    font-family: "Montserrat", Arial, sans-serif;
    font-weight: 600;
    font-size: 30px;
    letter-spacing: 3px;
    text-transform: uppercase;
    color: var(--gold);
  }
</style>
</head>
<body>
  <main class="book-cover">
    <h1 class="cover-title">Lasting<br>Harvest</h1>
    <div class="title-rule"></div>
    <p class="cover-subtitle">Growing riches beyond your years</p>
    <div class="cover-illustration" role="img" aria-label="Illustration of a golden upward arrow swirling through a rising stream of gold coins and sparkles"></div>
    <p class="cover-author">K. Dapo Ramiro</p>
  </main>
</body>
</html>
```